Meridale Legal Letterhead for Law firm must be modern and use the logo I uploaded.

Hello I want a clean modern professional letterhead for my law firm Meridale Legal. A logo has already been created and all files have been uploaded. The information for the firm can be given through message. Please use the logo that has already been created. Please also use the color scheme of that logo. (blue and white).

Target Market(s)

General Public

Industry/Entity Type

Law Firm

Colors

Designer to choose colors to be used in the design.

Requirements
Must have
• This must be a modern professional letterhead
Nice to have
• My logo that is included in file form
Should not have
• Should not have logo that is not the one I uploaded.

```html
<!DOCTYPE html>
<html lang="en">
<head>
<meta charset="utf-8">
<title>Meridale Legal Letterhead</title>
<link href="https://fonts.googleapis.com/css2?family=Open+Sans:wght@300;400;600&display=swap" rel="stylesheet">
<style>
  :root {
    --backdrop: #ececed;
    --paper: #f8f8f8;
    --navy: #2c3566;
    --ink: #6d6d70;
    --ink-soft: #8a8a8e;
  }
  * { box-sizing: border-box; margin: 0; padding: 0; }
  html, body {
    width: 1200px;
    height: 795px;
    overflow: hidden;
    background: var(--backdrop);
    font-family: "Open Sans", sans-serif;
  }
  .letterhead {
    position: absolute;
    left: 333px;
    top: 20px;
    width: 534px;
    height: 755px;
    background: var(--paper);
    box-shadow: 0 2px 10px rgba(0,0,0,0.08);
    padding: 0 52px;
  }
  .letterhead__header {
    display: flex;
    justify-content: space-between;
    align-items: flex-end;
    padding-top: 58px;
    padding-bottom: 14px;
    border-bottom: 1px solid var(--navy);
  }
  .brand-name {
    font-family: "Open Sans", sans-serif;
    font-weight: 400;
    font-size: 12px;
    letter-spacing: 0.42em;
    text-transform: uppercase;
    color: var(--navy);
    padding-bottom: 4px;
  }
  .contact {
    font-family: "Open Sans", sans-serif;
    font-weight: 300;
    font-size: 7.5px;
    line-height: 1.35;
    color: var(--ink-soft);
    text-align: left;
  }
  .contact__item {
    display: flex;
    align-items: center;
    gap: 4px;
  }
  .contact__icon {
    width: 7px;
    height: 7px;
    flex: none;
  }
  .letter {
    padding-top: 24px;
    font-size: 8.6px;
    line-height: 1.45;
    color: var(--ink);
  }
  .letter__greeting { margin-bottom: 12px; }
  .letter__paragraph { margin-bottom: 13px; padding-right: 14px; }
  .letter__closing { margin-top: 4px; }
  .signature {
    width: 80px;
    height: 44px;
    margin: 10px 0 0 28px;
    background: linear-gradient(135deg, rgba(44,53,102,0.10), rgba(44,53,102,0.22));
    border-radius: 3px;
  }
  .letterhead__footer-rule {
    position: absolute;
    left: 52px;
    right: 52px;
    bottom: 78px;
    border-top: 1.5px solid var(--navy);
  }
</style>
</head>
<body>
  <main class="letterhead">
    <header class="letterhead__header">
      <div class="brand-name">Meridale Legal</div>
      <address class="contact">
        <div>4820 Harlow Crest Road</div>
        <div>Suite 12 Pine Hollow,</div>
        <div>CO 80455</div>
        <div class="contact__item">
          <svg class="contact__icon" viewBox="0 0 10 10" aria-hidden="true"><path fill="#2c3566" d="M2 1h2l1 2.5-1.3 1a6 6 0 0 0 2.8 2.8l1-1.3L10 7v2c0 .6-.4 1-1 1A8 8 0 0 1 0 2c0-.6.4-1 1-1z"/></svg>
          <span>555.210.4738</span>
        </div>
        <div class="contact__item">
          <svg class="contact__icon" viewBox="0 0 10 10" aria-hidden="true"><rect x="0.5" y="2" width="9" height="6.5" rx="1" fill="#2c3566"/><path d="M1 2.6 5 5.6 9 2.6" stroke="#f8f8f8" stroke-width="0.9" fill="none"/></svg>
          <span>info@meridalelegal.com</span>
        </div>
        <div class="contact__item">
          <svg class="contact__icon" viewBox="0 0 10 10" aria-hidden="true"><circle cx="5" cy="5" r="4.5" fill="#2c3566"/><path d="M0.5 5h9M5 0.5c-2 2.5-2 6.5 0 9M5 0.5c2 2.5 2 6.5 0 9" stroke="#f8f8f8" stroke-width="0.7" fill="none"/></svg>
          <span>www.meridalelegal.com</span>
        </div>
      </address>
    </header>

    <section class="letter">
      <p class="letter__greeting">Dear customer,</p>
      <p class="letter__paragraph">Lorem ipsum dolor sit amet, consectetur adipisicing elit, sed do eiusmod tempor incididunt ut labore et dolore magna aliqua. Ut enim ad minim veniam, quis nostrud exercitation ullamco laboris nisi ut aliquip ex ea commodo consequat. Duis aute irure dolor in reprehenderit in voluptate velit esse cillum dolore eu fugiat nulla pariatur. Excepteur sint occaecat cupidatat non proident, sunt in culpa qui officia deserunt mollit anim id est laborum.</p>
      <p class="letter__paragraph">Lorem ipsum dolor sit amet, consectetur adipisicing elit, sed do eiusmod tempor incididunt ut labore et dolore magna aliqua. Ut enim ad minim veniam, quis nostrud exercitation ullamco laboris nisi ut aliquip ex ea commodo consequat. Duis aute irure dolor in reprehenderit in voluptate velit esse cillum dolore eu fugiat nulla pariatur. Excepteur sint occaecat cupidatat non proident, sunt in culpa qui officia deserunt mollit anim id est laborum.</p>
      <p class="letter__paragraph">Lorem ipsum dolor sit amet, consectetur adipisicing elit, sed do eiusmod tempor incididunt ut labore et dolore magna aliqua. Ut enim ad minim veniam, quis nostrud exercitation ullamco laboris nisi ut aliquip ex ea commodo consequat. Duis aute irure dolor in reprehenderit in voluptate velit esse cillum dolore eu fugiat nulla pariatur. Excepteur sint occaecat cupidatat non proident, sunt in culpa qui officia deserunt mollit anim id est laborum.</p>
      <p class="letter__paragraph">Lorem ipsum dolor sit amet, consectetur adipisicing elit, sed do eiusmod tempor incididunt ut labore et dolore magna aliqua. Ut enim ad minim veniam, quis nostrud exercitation ullamco laboris nisi ut aliquip ex ea commodo consequat. Duis aute irure dolor in reprehenderit.</p>
      <p class="letter__closing">Yours Sincerely,</p>
      <div class="signature" role="img" aria-label="Handwritten signature of the sender"></div>
    </section>

    <div class="letterhead__footer-rule"></div>
  </main>
</body>
</html>
```